Real Estate Web Page Redesign

We are a small town real estate agency in need of a web site redesign. To give you a little background on our agency…our target is middle income households and farmers. Our staff includes real estate agents and an auctioneer. We’ve been in business since 1997. We handle residential, commercial, recreational land and farmland.
Our current web site design is outdated and needs a more modern look. We are open to all design ideas but would want them to reflect our small town rural tradition and heritage.
The functionality and features of the site will remain the same. Your design will have to accommodate the existing features on the site. I have a programmer who will take the design you provide and retrofit the existing site functionality with it.
The deliverable will be a .psd file that can be converted to html for a site template. (We will do the conversion.)
The existing site is at:
http://www.tomwendelproperties.example/home.asp
Please take time to visit the site and note the current functionality the site has: property search, real estate news feed, mortgage rate feed, listings, navigation bar will need to handle existing links and expand to handle other future page links. The template provided will need to accommodate these features.
The current page logo can be used in the design or we are open to a redesign of that as well if needed to go with the design better.
Updates
Target Market(s)
Middle income households and farmers looking for the services of a real estate agent or auctioneer.
Industry/Entity Type
Real Estate
Look and feel
Each slider illustrates characteristics of the customer's brand and the style your logo design should communicate.

```html
<!DOCTYPE html>
<html lang="en">
<head>
<meta charset="utf-8">
<title>Wendel Real Estate and Land Company</title>
<link href="https://fonts.googleapis.com/css2?family=Arimo:wght@400;700&display=swap" rel="stylesheet">
<style>
:root{
  --navy:#123b7c;
  --navy-dark:#0e3370;
  --gold:#f5b700;
  --gold-light:#ffd84a;
  --ink:#333;
  --heading-blue:#163a7a;
  --panel:#e3f2fb;
  --panel-soft:#eef6fc;
  --cream:#fdf1cf;
  --white:#fff;
}
*{box-sizing:border-box;margin:0;padding:0}
html,body{width:1200px;height:1125px;overflow:hidden}
body{position:relative;background:var(--white);font-family:"Arimo",Arial,sans-serif;color:var(--ink)}
.sky{position:absolute;left:0;top:0;width:1200px;height:110px;background:linear-gradient(#cfe6f7,#fff)}
.brand{position:absolute;left:142px;top:50px;color:var(--navy);font-size:19px;line-height:22px;font-weight:400;display:flex;align-items:center;gap:8px}
.brand .mark{width:14px;height:14px;background:var(--navy)}
.brand small{display:block;font-size:13px;letter-spacing:2px}
.nav{position:absolute;left:346px;top:66px;width:712px;height:37px;display:flex;background:var(--navy)}
.nav a{flex:auto;color:var(--gold);text-decoration:none;font-size:14.5px;display:flex;align-items:center;justify-content:center;border-right:1px solid #5f86c4}
.nav a:last-child{border-right:0}
.nav a.active{background:linear-gradient(var(--gold-light),var(--gold));color:var(--navy-dark);flex:0 0 70px}
.hero{position:absolute;left:141px;top:104px;width:918px;height:278px;background:linear-gradient(#7fb7e6 0%,#b9d7ef 35%,#8a9a8c 55%,#4f7a3a 80%,#3f6a2c 100%)}
.welcome{position:absolute;left:157px;top:401px;width:562px}
h1{font-size:17.5px;font-weight:400;color:var(--heading-blue);margin:0 0 6px 1px}
.welcome p{font-size:12px;line-height:16.9px;text-align:justify}
h2{position:absolute;font-size:17px;font-weight:400;color:var(--gold)}
.premium{position:absolute;left:158px;top:626px;width:560px;height:176px;background:var(--panel)}
.card{position:absolute;top:12px;width:121px;text-align:center;font-size:12px;line-height:15px;color:#222}
.card .photo{width:121px;height:121px;margin-bottom:6px}
.arrow{position:absolute;top:68px;width:26px;height:26px;border-radius:50%;background:var(--white)}
.search{position:absolute;left:742px;top:396px;width:298px;height:292px;background:var(--panel)}
.search h3{height:34px;padding:7px 13px;font-size:17px;font-weight:400;color:var(--gold);background:#eaf5fc;border-bottom:1px solid #cfe3f1}
.row{position:absolute;left:17px;font-size:12px;color:#333;display:flex;align-items:center;width:266px;justify-content:space-between}
.select{width:159px;height:22px;background:var(--white);border:1px solid #c9d6df;position:relative;font-size:10px;padding:5px 8px}
.select::after{content:"";position:absolute;right:8px;top:7px;border:5px solid transparent;border-top:7px solid #222}
.band{position:absolute;left:0;top:182px;width:298px;height:20px;background:var(--navy);color:var(--gold);font-size:13px;text-align:center;line-height:20px}
.btn{position:absolute;top:257px;width:68px;height:22px;font-size:12px;text-align:center;line-height:22px}
.btn.gold{left:80px;background:linear-gradient(var(--gold-light),var(--gold));color:var(--navy-dark)}
.btn.blue{left:155px;background:var(--navy);color:var(--white)}
.news-signup{position:absolute;left:742px;top:707px;width:298px;height:94px;background:var(--navy)}
.news-signup h3{font-size:16px;font-weight:400;color:var(--white);padding:13px 14px}
.email{position:absolute;left:18px;top:44px;width:215px;height:24px;background:var(--white);font-size:10px;color:#555;padding:7px 14px}
.go{position:absolute;left:237px;top:44px;width:36px;height:24px;background:linear-gradient(var(--gold-light),#e69a00);color:var(--white);font-size:13px;text-align:center;line-height:24px}
.item{position:absolute;left:158px;width:280px;background:var(--panel-soft);font-size:12px;line-height:17px;padding:0 7px;text-align:justify}
.testi{position:absolute;left:449px;top:846px;width:269px;height:159px;background:var(--panel-soft);padding:8px 14px;font-size:12px;line-height:16px}
.testi p{text-align:justify}
.testi .by{text-align:right;margin-bottom:16px}
.testi .by span{color:var(--heading-blue)}
.rates{position:absolute;left:742px;top:845px;width:298px;border-collapse:collapse;font-size:12px}
.rates th{height:44px;background:linear-gradient(var(--gold-light),var(--gold));font-weight:400;text-align:left;color:#222;padding:0 10px;line-height:16px;vertical-align:middle}
.rates td{height:21.6px;background:var(--cream);padding:0 10px;border-left:2px solid var(--white)}
.rates td:first-child{border-left:0;width:109px}
.rates td:nth-child(2){padding-left:34px;width:95px}
.rates td:last-child{text-align:right}
.rates tr:first-child td{padding-top:4px}
footer{position:absolute;left:0;top:1031px;width:1200px;height:94px;background:var(--navy);text-align:center;color:var(--gold);font-size:11px}
footer nav{margin-top:14px;display:flex;justify-content:center;gap:19px;font-size:10.5px}
footer p{line-height:15px}
footer .legal{margin-top:26px}
</style>
</head>
<body>
<div class="sky"></div>
<div class="brand"><span class="mark"></span><div>WENDEL REAL ESTATE<small>and Land Company</small></div></div>
<nav class="nav">
  <a class="active">Home</a><a>About us</a><a>Open Houses</a><a>Calculator/Links</a><a>Testimonials</a><a>Latest News</a><a>Contact us</a>
</nav>
<div class="hero" role="img" aria-label="Photograph of a single-storey house with a gray roof, green lawn and trees under a blue sky"></div>

<section class="welcome">
  <h1>Welcome to Wendel Real Estate and Land Company</h1>
  <p>Your visit here will make it easy for you to find the real estate you are seeking by using our simple search menu. Not only will you find area real estate listings, but also other items such as the latest mortgage rates and real estate news, and businesses that are associated with buying and selling homes and farmland. I will be servicing the needs of the people in the Galva, Bishop Hill, Cambridge, Kewanee, Woodhull and all area communities. I have been in the real estate business since 1997 and have been a broker since 1999. I’m looking forward to marketing your property for "top dollar" or finding that "perfect" piece of property you desire whether it be residential, commercial, recreational, farmland (statewide), country property, or 1031 exchange. I am also a member of the Prairie County Multiple Listing Service.</p>
</section>

<h2 style="left:159px;top:598px">Premium Listing</h2>
<section class="premium">
  <div class="card" style="left:16px"><div class="photo" role="img" aria-label="Photo of a large white villa with pool" style="background:linear-gradient(#8fc3ea,#e8d9b8 60%,#5aa7d6)"></div>3 Bedroom<br>Galva $93,900</div>
  <div class="card" style="left:151px"><div class="photo" role="img" aria-label="Photo of a two-storey house with lawn" style="background:linear-gradient(#a9cbe8,#7d8f7a 50%,#4f8a35)"></div>3 Bedroom<br>Galva $93,900</div>
  <div class="card" style="left:285px"><div class="photo" role="img" aria-label="Photo of a single-storey house among palm trees" style="background:linear-gradient(#8fbfe6,#c9c2a5 50%,#5c9a3a)"></div>3 Bedroom<br>Galva $93,900</div>
  <div class="card" style="left:422px"><div class="photo" role="img" aria-label="Photo of a white two-storey house" style="background:linear-gradient(#d7e3ee,#c9ccd2 55%,#6f9a4e)"></div>3 Bedroom<br>Galva $93,900</div>
  <div class="arrow" style="left:-4px"><svg width="26" height="26"><path d="M8 13l8-6v12z" fill="#123b7c"/></svg></div>
  <div class="arrow" style="left:536px"><svg width="26" height="26"><path d="M18 13l-8-6v12z" fill="#123b7c"/></svg></div>
</section>

<aside class="search">
  <h3>Search Our Listings</h3>
  <div class="row" style="top:48px">Property Type<span class="select"></span></div>
  <div class="row" style="top:79px">No. of Bedrooms<span class="select"></span></div>
  <div class="row" style="top:110px">City<span class="select"></span></div>
  <div class="row" style="top:141px">Price<span class="select"></span></div>
  <div class="band">Or to see all listings, just click "Search"</div>
  <div class="row" style="top:221px">Pick a Listing<span class="select">Listing Number</span></div>
  <div class="btn gold">Search</div><div class="btn blue">Reset</div>
</aside>

<aside class="news-signup">
  <h3>Sign up for Newsletter</h3>
  <div class="email">enter your email id</div><div class="go">Go</div>
</aside>

<h2 style="left:158px;top:820px">Latest News</h2>
<div class="item" style="top:846px;height:51px;padding-top:8px">Area Bank Halts Cash-out Refinancing; Letters From the Trenches; Mortgage Hiring...</div>
<div class="item" style="top:899px;height:51px;padding-top:8px">Mortgages Rates Higher Again and Less Consistent Between Lenders...</div>
<div class="item" style="top:953px;height:51px;padding-top:6px;padding-left:10px">Momentum Seen for Home Improvement Spending...</div>

<h2 style="left:452px;top:820px">Testimonials</h2>
<section class="testi">
  <p>Lorem Ipsum is simply dummy text of the printing and typesetting industry. Lorem Ipsum has been the industry's</p>
  <p class="by">by <span>Lorem Ipsum</span></p>
  <p>Lorem Ipsum is simply dummy text of the printing and typesetting industry. Lorem Ipsum has been the industry's</p>
  <p class="by">by <span>Lorem Ipsum</span></p>
</section>

<h2 style="left:742px;top:820px">Mortgage Rates</h2>
<table class="rates">
  <tr><th>NATIONAL<br>AVERAGES</th><th style="padding-left:34px;vertical-align:bottom;padding-bottom:6px">%</th><th></th></tr>
  <tr><td>30 Yr Fixed</td><td>4.56%</td><td>-0.01%</td></tr>
  <tr><td>15 Yr Fixed</td><td>4.03%</td><td>-0.03%</td></tr>
  <tr><td>1 Yr ARM</td><td>3.70%</td><td>-0.04%</td></tr>
  <tr><td>Fed Prime</td><td>3.25%</td><td>0.00%</td></tr>
  <tr><td>30 Yr Tres</td><td>4.08%</td><td>0.00%</td></tr>
</table>

<footer>
  <nav><span>Home</span><span>About us</span><span>Open Houses</span><span>Calculator/Links</span><span>Testimonials</span><span>Latest News</span><span>Contact us</span></nav>
  <p class="legal">All Rights Reserved</p>
  <p>© 2012 Wendel Real Estate and Land Company</p>
</footer>
</body>
</html>
```